Business card design Needed for new logo / Construction business, home extensions and new builds

We need a business card design using our new logo files which i will attach to this project :)

We are a small construction business specialising in home extensions, new builds and property development. We are very ambitious and would appreciate professional and elegant designs for our new business card.

Very serious about using the services on BriefNest and recently acquired our new logo from here :)

Please get involved, i will feedback when i can as i am very busy but can respond daily, thanks

Target Market(s)

People that want to build onto their houses, new building developments or adding too their existing property

Industry/Entity Type

Construction

Contact Information for Business Card

Hollin Marsh Construction, Tobias Renwick (Managing Director), Tel 07822200444, email - info@hollin-marsh, www.hollin-marsh.co.uk

Colors

Designer to choose colors to be used in the design.

Requirements
Must have
• I like a deep grey on the back please. A lot of you have provided black from and back, try mixing things up a little. The black looks cool 😎 Thanks

```html
<!DOCTYPE html>
<html lang="en">
<head>
<meta charset="utf-8">
<title>Hollin Marsh Construction – Business Card</title>
<link rel="stylesheet" href="https://fonts.googleapis.com/css2?family=Cinzel:wght@400;600&family=Didact+Gothic&display=swap">
<style>
  :root {
    --backdrop: #d0d5d8;
    --card: #262f3f;
    --gold: #dfac4d;
    --silver: #a7abb2;
    --white: #ffffff;
  }
  * { margin: 0; padding: 0; box-sizing: border-box; }
  html, body {
    width: 1200px; height: 960px; overflow: hidden;
    background: var(--backdrop);
  }
  .canvas { position: relative; width: 1200px; height: 960px; }
  .card {
    position: absolute; left: 302px; width: 596px; height: 340px;
    background: var(--card); overflow: hidden;
  }
  .card--front { top: 116px; }
  .card--back { top: 506px; }

  /* front */
  .brand-mark {
    position: absolute; right: 48px; top: 62px;
    display: flex; align-items: center; gap: 8px;
    font-family: "Cinzel", serif; font-weight: 600; font-size: 16px;
    letter-spacing: 1px; color: var(--gold);
  }
  .brand-mark__square { width: 10px; height: 10px; background: var(--gold); }
  .person-name {
    position: absolute; left: 45px; top: 168px;
    font-family: "Cinzel", serif; font-weight: 400; font-size: 30px;
    color: var(--white); line-height: 1;
  }
  .person-role {
    position: absolute; left: 48px; top: 200px;
    font-family: "Didact Gothic", sans-serif; font-size: 15px;
    letter-spacing: 10px; color: var(--white); line-height: 1;
  }
  .divider {
    position: absolute; left: 49px; top: 223px; width: 498px; height: 2px;
    background: var(--gold);
  }
  .contact-list {
    position: absolute; left: 49px; top: 236px; list-style: none;
    font-family: "Didact Gothic", sans-serif; font-size: 15.5px;
    color: var(--white); letter-spacing: 0.5px;
  }
  .contact-list li { display: flex; align-items: center; height: 20px; }
  .contact-list svg { width: 14px; height: 14px; margin-right: 10px; flex: none; }
  .contact-list .web { color: var(--gold); }
  .address {
    position: absolute; right: 48px; top: 256px; text-align: right;
    font-family: "Didact Gothic", sans-serif; font-size: 15.5px;
    color: var(--white); line-height: 20px; letter-spacing: 0.3px;
  }
  .address svg { width: 12px; height: 15px; vertical-align: -2px; margin-right: 4px; }
  .card-footer { position: absolute; left: 0; bottom: 0; width: 596px; height: 30px; }

  /* back */
  .wordmark {
    position: absolute; left: 0; right: 0; top: 118px; text-align: center;
    font-family: "Cinzel", serif; font-weight: 600; color: var(--gold);
  }
  .wordmark__square { width: 14px; height: 14px; background: var(--gold); margin: 0 auto 22px; }
  .wordmark__name { font-size: 32px; letter-spacing: 1px; line-height: 1.1; }
  .wordmark__trade { font-size: 20px; letter-spacing: 1px; margin-top: 6px; }
</style>
</head>
<body>
<main class="canvas">
  <section class="card card--front" aria-label="Business card front">
    <div class="brand-mark"><span class="brand-mark__square"></span>Hollin Marsh</div>

    <h1 class="person-name">YOUR NAME</h1>
    <p class="person-role">DIRECTOR</p>
    <div class="divider"></div>

    <ul class="contact-list">
      <li>
        <svg viewBox="0 0 24 24" aria-hidden="true"><path fill="#dfac4d" d="M6.6 10.8a15.1 15.1 0 0 0 6.6 6.6l2.2-2.2a1 1 0 0 1 1-.25 11.4 11.4 0 0 0 3.6.57 1 1 0 0 1 1 1V20a1 1 0 0 1-1 1A17 17 0 0 1 3 4a1 1 0 0 1 1-1h3.5a1 1 0 0 1 1 1c0 1.25.2 2.45.57 3.57a1 1 0 0 1-.25 1z"/></svg>
        0044 161 4307729
      </li>
      <li>
        <svg viewBox="0 0 24 24" aria-hidden="true"><rect x="2" y="5" width="20" height="14" fill="none" stroke="#dfac4d" stroke-width="2"/><path d="M2 5l10 8 10-8M2 19l7-7M22 19l-7-7" fill="none" stroke="#dfac4d" stroke-width="2"/></svg>
        info@hollin-marsh.es
      </li>
      <li class="web">
        <svg viewBox="0 0 24 24" aria-hidden="true"><g fill="none" stroke="#dfac4d" stroke-width="1.6"><circle cx="12" cy="12" r="9"/><ellipse cx="12" cy="12" rx="4" ry="9"/><path d="M3 12h18M4.5 7.5h15M4.5 16.5h15"/></g></svg>
        www.hollin-marsh.es
      </li>
    </ul>

    <p class="address">
      <svg viewBox="0 0 12 16" aria-hidden="true"><path fill="#dfac4d" d="M6 0a6 6 0 0 0-6 6c0 4.5 6 10 6 10s6-5.5 6-10a6 6 0 0 0-6-6zm0 8.5A2.5 2.5 0 1 1 6 3.5a2.5 2.5 0 0 1 0 5z"/></svg>Calle Mirador 14 –<br>Altea (Paseo del Puerto)
    </p>

    <svg class="card-footer" viewBox="0 0 596 30" aria-hidden="true">
      <path d="M0 5h372l-20 6H0z" fill="#a7abb2"/>
      <path d="M0 20h350l48-17h198v27H0z" fill="#dfac4d"/>
    </svg>
  </section>

  <section class="card card--back" aria-label="Business card back">
    <div class="wordmark">
      <div class="wordmark__square"></div>
      <div class="wordmark__name">HOLLIN MARSH</div>
      <div class="wordmark__trade">CONSTRUCTION</div>
    </div>
  </section>
</main>
</body>
</html>
```